Australian Civil Construction, Quarry & Mining Services needs a business card

We need a business card designed for our Civil Construction, Quarry & Mining Services based in the country in Australia.
Our Company Brindle Earthworks provide innovate solutions for infrastructure, agricultural and mining (aggregate, sand, roadbase) industry.
We would like our business cards to be double sided
Front of card: black background or something that resembles our business colours. (it doesn't have to be black we are open to options)
- Company name - Brindle Earthworks
- Either our logo or some sort of icon/picture that resembles our business
- Website - https://brindleearthworks-example.com.au/
- We will have a number of different names, positions descriptions, phone numbers and emails on separate cards for each of our managers/directors

```html
<!DOCTYPE html>
<html lang="en">
<head>
<meta charset="utf-8">
<title>Brindle Earthworks – Business Card</title>
<link href="https://fonts.googleapis.com/css2?family=Roboto:wght@400;500&display=swap" rel="stylesheet">
<style>
  :root {
    --bg: #2a2a2c;
    --card-black: #151314;
    --brand-orange: #d85c1c;
    --accent-orange: #f47f1e;
    --white: #ffffff;
  }
  * { box-sizing: border-box; margin: 0; padding: 0; }
  html, body {
    width: 1200px; height: 900px; overflow: hidden;
    background: var(--bg);
    font-family: "Roboto", Arial, sans-serif;
  }
  .stage {
    width: 1200px; height: 900px;
    display: flex; flex-direction: column;
    align-items: center; justify-content: center; gap: 56px;
  }
  .card {
    position: relative;
    width: 600px; height: 367px;
    overflow: hidden;
    box-shadow: 0 10px 28px rgba(0,0,0,0.45);
  }
  .card-front { background: var(--brand-orange); }
  .card-back {
    background: var(--card-black);
    display: flex; align-items: center; justify-content: center;
  }
  .front-curve { position: absolute; inset: 0; }
  .contact {
    position: absolute; left: 40px; top: 52px;
    color: var(--white);
  }
  .contact-name { font-size: 31px; font-weight: 500; letter-spacing: 0.5px; line-height: 1; }
  .contact-role { font-size: 15px; font-weight: 400; margin-top: 4px; letter-spacing: 0.5px; }
  .contact-address { font-size: 15px; margin-top: 18px; line-height: 1.35; }
  .contact-list { list-style: none; margin-top: 14px; font-size: 13.5px; line-height: 1.6; }
  .contact-list li { display: flex; align-items: center; gap: 7px; white-space: nowrap; }
  .contact-list svg { width: 12px; height: 12px; flex: none; }
  .brand {
    position: absolute; right: 30px; top: 205px;
    display: flex; align-items: center; gap: 12px;
  }
  .brand-mark { width: 20px; height: 20px; background: var(--accent-orange); flex: none; }
  .brand-name {
    color: var(--white); font-size: 22px; font-weight: 500;
    letter-spacing: 2px; text-transform: uppercase; line-height: 1.15;
  }
  .card-back .brand { position: static; }
  .card-back .brand-mark { width: 30px; height: 30px; }
  .card-back .brand-name { font-size: 30px; }
</style>
</head>
<body>
<main class="stage">
  <section class="card card-front">
    <svg class="front-curve" viewBox="0 0 600 367" aria-hidden="true">
      <circle cx="700" cy="400" r="400" fill="var(--white)"/>
      <circle cx="706" cy="398" r="390" fill="var(--card-black)"/>
    </svg>
    <div class="contact">
      <p class="contact-name">DARCY HOLLOWAY</p>
      <p class="contact-role">PRESIDENT</p>
      <p class="contact-address">14 Coolabah Lane, Yarrawin<br>Victoria 3799, Australia</p>
      <ul class="contact-list">
        <li>
          <svg viewBox="0 0 24 24"><path fill="#fff" d="M6.6 10.8a15 15 0 0 0 6.6 6.6l2.2-2.2c.3-.3.7-.4 1-.2 1.1.4 2.3.6 3.6.6.6 0 1 .4 1 1V20c0 .6-.4 1-1 1A17 17 0 0 1 3 4c0-.6.4-1 1-1h3.5c.6 0 1 .4 1 1 0 1.3.2 2.5.6 3.6.1.3 0 .7-.2 1z"/></svg>
          03 5700 1188
        </li>
        <li>
          <svg viewBox="0 0 24 24"><rect x="2" y="5" width="20" height="14" fill="none" stroke="#fff" stroke-width="2"/><path d="M2 5l10 8 10-8" fill="none" stroke="#fff" stroke-width="2"/></svg>
          office@brindle-example.com.au
        </li>
        <li>
          <svg viewBox="0 0 24 24"><circle cx="12" cy="12" r="10" fill="none" stroke="#fff" stroke-width="2"/><ellipse cx="12" cy="12" rx="4" ry="10" fill="none" stroke="#fff" stroke-width="2"/><path d="M2 12h20" stroke="#fff" stroke-width="2"/></svg>
          brindleearthworks-example.com.au
        </li>
      </ul>
    </div>
    <div class="brand">
      <span class="brand-mark" aria-hidden="true"></span>
      <span class="brand-name">Brindle<br>Earthworks</span>
    </div>
  </section>

  <section class="card card-back">
    <div class="brand">
      <span class="brand-mark" aria-hidden="true"></span>
      <span class="brand-name">Brindle Earthworks</span>
    </div>
  </section>
</main>
</body>
</html>
```